Business Card Design Project

I need a business card design for my law office. I already have a logo.

I am an employment attorney who represents clients who have been wrongfully terminated or have been discriminated against by their employer.

I would like a unique, clean design using the colors in the logo or colors that complement the logo.

Target Market(s)

Clients, potential clients, other attorneys and others.

Industry/Entity Type

Attorney

Requirements
Must have
• I would like to use both sides of the card.

The information on the card must be easy to read.

Here is my information:

T. Dale Everhoff
3857 E. Pallister Rd., Suite 204
Fresno, California 93703
559-731-4086
559-862-5143 fax
dale@lawtde.example
Nice to have
• QR Code? I would like to see designs incorporating a nice-looking QR code. Look at this example:

Notice the second QR code in the article - the color.

```html
<!DOCTYPE html>
<html lang="en">
<head>
<meta charset="utf-8">
<title>Everhoff Law Office – Business Card</title>
<link href="https://fonts.googleapis.com/css2?family=Open+Sans:wght@400;600&display=swap" rel="stylesheet">
<style>
  :root {
    --page-bg: #ffffff;
    --brand-blue: #29a8df;
    --brand-blue-light: #45c2ef;
    --brand-blue-deep: #1f93cc;
    --card-white: #f7f7f8;
    --card-grey: #e4e5e7;
    --text-grey: #6d6f72;
    --rule-grey: #8a8c8f;
    --band-grey: #6b6d70;
    --shadow: rgba(0, 0, 0, 0.18);
  }
  * { box-sizing: border-box; margin: 0; padding: 0; }
  html, body {
    width: 1200px; height: 871px; overflow: hidden;
    background: var(--page-bg);
    font-family: "Open Sans", Arial, sans-serif;
  }
  .canvas {
    position: relative; width: 1200px; height: 871px;
  }
  .card {
    position: absolute; left: 335px; width: 530px; height: 300px;
    border-radius: 22px; overflow: hidden;
    box-shadow: 0 6px 18px var(--shadow);
  }
  /* Front side */
  .card--front {
    top: 120px;
    background: radial-gradient(ellipse at 55% 45%, var(--brand-blue-light) 0%, var(--brand-blue) 70%, var(--brand-blue-deep) 100%);
  }
  .brand {
    position: absolute; display: flex; align-items: center;
    font-weight: 400; white-space: nowrap;
  }
  .brand__square { display: block; flex: none; }
  .card--front .brand {
    left: 52px; top: 128px; gap: 18px;
    color: #ffffff; font-size: 38px; letter-spacing: -0.5px;
  }
  .card--front .brand__square { width: 44px; height: 44px; background: #ffffff; }

  /* Back side */
  .card--back {
    top: 470px;
    background: linear-gradient(180deg, var(--card-white) 0%, var(--card-grey) 100%);
  }
  .card--back .brand {
    left: 44px; top: 44px; gap: 10px;
    color: var(--brand-blue); font-size: 27px; letter-spacing: -0.3px;
  }
  .card--back .brand__square { width: 30px; height: 30px; background: var(--brand-blue); }
  .holder-name {
    position: absolute; left: 34px; top: 158px;
    color: var(--brand-blue); font-size: 17px; font-weight: 400;
  }
  .holder-rule {
    position: absolute; left: 34px; top: 188px; width: 352px; height: 1px;
    background: var(--rule-grey);
  }
  .contact-list { position: absolute; left: 34px; top: 212px; list-style: none; }
  .contact-list li {
    display: flex; align-items: center; gap: 10px;
    color: var(--text-grey); font-size: 11px; height: 26px;
  }
  .contact-icon { width: 16px; height: 16px; flex: none; }
  .info-band {
    position: absolute; left: 0; bottom: 0; width: 100%; height: 26px;
  }
  .info-band svg { position: absolute; inset: 0; }
  .info-band__address {
    position: absolute; left: 14px; top: 5px;
    color: #ffffff; font-size: 10.5px; white-space: nowrap;
  }
  .info-band__email {
    position: absolute; right: 28px; top: 5px;
    color: var(--brand-blue-light); font-size: 11px;
  }
</style>
</head>
<body>
<main class="canvas">

  <section class="card card--front" aria-label="Card front">
    <div class="brand">
      <span class="brand__square"></span>
      <span class="brand__name">Everhoff Law Office</span>
    </div>
  </section>

  <section class="card card--back" aria-label="Card back">
    <div class="brand">
      <span class="brand__square"></span>
      <span class="brand__name">Everhoff Law Office</span>
    </div>

    <p class="holder-name">T. Dale Everhoff</p>
    <div class="holder-rule"></div>

    <ul class="contact-list">
      <li>
        <svg class="contact-icon" viewBox="0 0 16 16" aria-hidden="true">
          <rect width="16" height="16" rx="3" fill="#29a8df"/>
          <path d="M5 3.5h2l1 2.5-1.3 1a6 6 0 0 0 2.3 2.3l1-1.3 2.5 1v2a1 1 0 0 1-1 1A8.5 8.5 0 0 1 4 4.5a1 1 0 0 1 1-1z" fill="#fff"/>
        </svg>
        <span>559-731-4086</span>
      </li>
      <li>
        <svg class="contact-icon" viewBox="0 0 16 16" aria-hidden="true">
          <rect width="16" height="16" rx="3" fill="#29a8df"/>
          <rect x="4" y="3" width="8" height="4" fill="#fff"/>
          <rect x="3" y="7" width="10" height="5" rx="1" fill="#fff"/>
          <rect x="5" y="9" width="6" height="4" fill="#29a8df"/>
        </svg>
        <span>559-862-5143</span>
      </li>
    </ul>

    <div class="info-band">
      <svg width="530" height="26" viewBox="0 0 530 26" preserveAspectRatio="none" aria-hidden="true">
        <polygon points="0,0 318,0 300,26 0,26" fill="#29a8df"/>
        <polygon points="324,0 530,0 530,26 306,26" fill="#6b6d70"/>
      </svg>
      <span class="info-band__address">3857 E. Pallister Rd., Suite 204 Fresno, California 93703</span>
      <span class="info-band__email">dale@lawtde.example</span>
    </div>
  </section>

</main>
</body>
</html>
```